Business Card Revision

Need to redesign my business cards for a new professional look. We are a courier company. You can go to www.qvrunners.com to see what we do. The trucks have an old company name (Sprout) on them but that is the company we are just now
changing the name.

Target Market(s)

Potential clients. We service the automotive, plumbing, printing, air freight industries as well as many others.

Industry/Entity Type

Business

Contact Information for Business Card

QVmotion
20864 Lark Fenmore Parkway
Fenwick, Oh 45873

Thomas R. Wendall
President

tom@qvrunners.com

Main: (555) 555-0147

```html
<!DOCTYPE html>
<html lang="en">
<head>
<meta charset="utf-8">
<title>QV Runners — Business Card</title>
<link rel="stylesheet" href="https://fonts.googleapis.com/css2?family=Source+Sans+3:wght@400;600;700&display=swap">
<style>
  :root {
    --backdrop: #d9d9d9;
    --card: #0b0b0b;
    --card-edge: #1a1a1a;
    --white: #ffffff;
    --soft-white: #e9e9e9;
    --brand-blue: #1f7fc9;
    --brand-green: #3dbb3f;
    --rule: #3a3a3a;
  }
  * { margin: 0; padding: 0; box-sizing: border-box; }
  html, body {
    width: 1200px;
    height: 900px;
    overflow: hidden;
    background: var(--backdrop);
    font-family: "Source Sans 3", "Myriad Pro", Arial, sans-serif;
  }
  .canvas {
    position: relative;
    width: 1200px;
    height: 900px;
  }
  .card {
    position: absolute;
    left: 250px;
    width: 700px;
    height: 400px;
    background: radial-gradient(ellipse at 55% 40%, var(--card-edge) 0%, var(--card) 70%);
    box-shadow: 0 6px 18px rgba(0,0,0,0.25);
  }
  .card--front { top: 30px; }
  .card--back  { top: 470px; }

  .wordmark {
    position: absolute;
    font-weight: 700;
    letter-spacing: 0.08em;
    text-transform: uppercase;
    white-space: nowrap;
  }
  .card--front .wordmark {
    left: 0; right: 0;
    top: 160px;
    text-align: center;
    font-size: 64px;
    line-height: 80px;
    color: var(--white);
  }
  .card--back .wordmark {
    left: 360px;
    top: 78px;
    font-size: 40px;
    line-height: 50px;
    color: var(--brand-green);
  }

  .holder {
    position: absolute;
    left: 56px;
    top: 118px;
  }
  .holder__name {
    font-size: 23px;
    font-weight: 600;
    color: var(--brand-blue);
    line-height: 26px;
  }
  .holder__title {
    font-size: 15px;
    color: var(--soft-white);
    line-height: 18px;
  }
  .name-rule {
    position: absolute;
    left: 250px;
    top: 146px;
    width: 390px;
    height: 1px;
    background: linear-gradient(90deg, var(--rule), rgba(58,58,58,0.2));
  }
  .contact-rule {
    position: absolute;
    left: 400px;
    top: 226px;
    width: 240px;
    height: 1px;
    background: var(--rule);
  }
  .contacts {
    position: absolute;
    right: 60px;
    top: 236px;
    list-style: none;
    text-align: right;
  }
  .contacts li {
    display: flex;
    justify-content: flex-end;
    align-items: center;
    gap: 10px;
    font-size: 18px;
    line-height: 24px;
    color: var(--white);
  }
  .contacts .icon {
    width: 14px;
    height: 14px;
    flex: none;
  }
  .contacts .spacer { width: 14px; flex: none; }
</style>
</head>
<body>
<main class="canvas">

  <section class="card card--front" aria-label="Card front">
    <div class="wordmark">QV Runners</div>
  </section>

  <section class="card card--back" aria-label="Card back">
    <div class="wordmark">QV Runners</div>

    <div class="holder">
      <p class="holder__name">Thomas R. Wendall</p>
      <p class="holder__title">President</p>
    </div>
    <div class="name-rule"></div>

    <div class="contact-rule"></div>
    <ul class="contacts">
      <li>(555) 555-0147
        <svg class="icon" viewBox="0 0 24 24" aria-hidden="true"><path fill="#1f7fc9" d="M6.6 10.8a15.1 15.1 0 0 0 6.6 6.6l2.2-2.2a1 1 0 0 1 1-.25 11.4 11.4 0 0 0 3.6.57 1 1 0 0 1 1 1V20a1 1 0 0 1-1 1A17 17 0 0 1 3 4a1 1 0 0 1 1-1h3.5a1 1 0 0 1 1 1c0 1.25.2 2.45.57 3.6a1 1 0 0 1-.25 1z"/></svg>
      </li>
      <li>tom@qvrunners.com
        <svg class="icon" viewBox="0 0 24 24" aria-hidden="true"><rect x="2" y="5" width="20" height="14" rx="1.5" fill="#1f7fc9"/><path d="M3 6l9 7 9-7" fill="none" stroke="#0b0b0b" stroke-width="1.8"/></svg>
      </li>
      <li>www.qvrunners.com
        <svg class="icon" viewBox="0 0 24 24" aria-hidden="true"><circle cx="12" cy="12" r="10" fill="#1f7fc9"/><path d="M2 12h20M12 2c3 3 3 17 0 20M12 2c-3 3-3 17 0 20" fill="none" stroke="#0b0b0b" stroke-width="1.4"/></svg>
      </li>
      <li>20864 Lark Fenmore Parkway<span class="spacer"></span></li>
      <li>Fenwick, Oh 45873<span class="spacer"></span></li>
    </ul>
  </section>

</main>
</body>
</html>
```